Real-Estate business needs e-newsletter design for mail-chimp

We need a newsletter design as a PSD file.

Features of the e-newsletter design should include;

1. Our Corporate Colours and Logo - refer www.quellbrook.com.au
2. Our website menu items so readers can reference our services
3. Format should include our newsletter articles - usually 2 or 3 articles
4. Format should include a "special offer" section
5. Format should include our facebook likes widget as it appears on our website
6. Format should include company directors profile with "linked in" icon

```html
<!DOCTYPE html>
<html lang="en">
<head>
<meta charset="utf-8">
<title>Quellbrook Property Newsletter</title>
<link rel="stylesheet" href="https://fonts.googleapis.com/css2?family=Arimo:wght@400;700&family=Open+Sans:wght@400;600;700&display=swap">
<style>
:root{
  --brand-blue:#2f5b9e;
  --button-blue:#325f9f;
  --offer-blue:rgba(38,82,160,.92);
  --offer-yellow:#f7c744;
  --text-dark:#222;
  --text-grey:#6f6f6f;
  --heading-grey:#555a60;
  --section-grey:#f4f4f4;
  --footer-grey:#f1f1f1;
  --rule:#e3e3e3;
  --black:#000;
  --white:#fff;
}
*{margin:0;padding:0;box-sizing:border-box}
html,body{width:1200px;height:2920px;overflow:hidden;background:var(--white)}
body{position:relative;font-family:"Arimo",Arial,sans-serif;color:var(--text-dark)}
.abs{position:absolute}

/* header */
.brand-name{left:60px;top:44px;font-size:44px;font-weight:400;letter-spacing:1px;color:#333;white-space:nowrap}
.call-us{right:64px;top:40px;font-family:"Open Sans",sans-serif;font-weight:700;font-size:34px;color:var(--brand-blue);display:flex;align-items:center;gap:14px;white-space:nowrap}
.view-note{right:70px;top:94px;font-family:"Open Sans",sans-serif;font-size:22px;color:#8a8a8a;white-space:nowrap}
.view-note span{text-decoration:underline}

/* hero offer */
.hero-photo{left:60px;top:154px;width:1080px;height:568px;background:linear-gradient(180deg,#5b90d8 0%,#a9c8ec 42%,#c9c6bd 62%,#5f8f3b 82%,#4b7a2c 100%)}
.offer-box{left:60px;top:294px;width:540px;height:336px;background:var(--offer-blue);padding:44px 44px;color:var(--white);font-weight:700;font-size:64px;line-height:86px;white-space:nowrap}
.offer-box em{font-style:normal;color:var(--offer-yellow)}

/* intro */
.intro{left:0;top:774px;width:1200px;text-align:center;font-size:26px;line-height:42px;color:var(--text-grey);white-space:nowrap}
.intro b{color:#555}
.benefit{top:904px;width:300px;text-align:center}
.benefit svg{display:block;margin:0 auto}
.benefit p{margin-top:30px;font-size:23px;font-weight:700;line-height:40px;color:var(--black)}

/* articles */
.articles{left:0;top:1268px;width:1200px;height:856px;background:var(--section-grey);border-top:2px solid var(--rule);border-bottom:2px solid var(--rule)}
.section-title{font-size:46px;font-weight:700;color:var(--heading-grey);white-space:nowrap}
.articles-title{left:60px;top:1316px}
.article-photo{top:1410px;width:510px;height:240px}
.article-title{top:1680px;font-size:36px;font-weight:700;color:var(--brand-blue)}
.article-body{top:1746px;width:510px;font-size:22px;line-height:36px;color:var(--text-grey)}
.read-more{top:1938px;width:158px;height:70px;background:var(--button-blue);color:var(--white);font-size:22px;font-weight:700;display:flex;align-items:center;justify-content:center}

/* director */
.director-photo{left:60px;top:2176px;width:232px;height:232px;border-radius:50%;background:radial-gradient(circle at 50% 40%,#d9b9a2 0%,#b88d74 35%,#e9e9ec 36%,#f4f4f6 70%,#2d3240 71%)}
.director-title{left:334px;top:2182px}
.director-bio{left:334px;top:2256px;width:770px;font-size:22px;line-height:36px;color:var(--text-grey)}
.social-square{top:2396px;width:64px;height:64px;border-radius:6px}

/* footer */
.footer{left:0;top:2528px;width:1200px;height:288px;background:var(--footer-grey)}
.widget-photo{left:84px;top:2588px;width:84px;height:92px;background:linear-gradient(180deg,#ececec 0%,#cfa68c 45%,#2e3442 80%)}
.widget-name{left:176px;top:2590px;font-size:22px;font-weight:700;color:var(--brand-blue);white-space:nowrap}
.like-btn{left:176px;top:2630px;width:94px;height:38px;border-radius:4px;background:#4a66a8;color:var(--white);font-size:21px;font-weight:700;display:flex;align-items:center;justify-content:center;gap:6px}
.like-btn i{width:16px;height:16px;background:var(--white);border-radius:2px;display:block}
.widget-rule{left:56px;top:2702px;width:320px;height:2px;background:#d4d4d4}
.widget-count{left:56px;top:2716px;font-size:19px;color:#222;white-space:nowrap}
.widget-count span{color:var(--brand-blue)}
.menu-head{top:2582px;font-family:"Open Sans",sans-serif;font-size:23px;color:#444;white-space:nowrap}
.menu-list{top:2634px;list-style:none;font-family:"Open Sans",sans-serif;font-size:22px;color:var(--brand-blue);white-space:nowrap}
.menu-list li{height:52px;display:flex;align-items:center;gap:12px}
.menu-list li::before{content:"";width:9px;height:9px;border-right:3px solid #8a8a8a;border-top:3px solid #8a8a8a;transform:rotate(45deg)}

.bottom-bar{left:0;top:2816px;width:1200px;height:104px;background:var(--black);color:#ddd;font-size:22px;display:flex;align-items:center;justify-content:space-between;padding:0 62px 0 60px}
</style>
</head>
<body>

<header>
  <div class="abs brand-name">QUELLBROOK PROPERTY</div>
  <div class="abs call-us">
    <svg width="30" height="30" viewBox="0 0 24 24" aria-hidden="true"><path fill="#a3a3a3" d="M6.6 10.8a15 15 0 0 0 6.6 6.6l2.2-2.2c.3-.3.7-.4 1-.2 1.1.4 2.3.6 3.6.6.6 0 1 .4 1 1V20c0 .6-.4 1-1 1A17 17 0 0 1 3 4c0-.6.4-1 1-1h3.5c.6 0 1 .4 1 1 0 1.3.2 2.5.6 3.6.1.3 0 .7-.2 1z"/></svg>
    Call us: 1300 555 019
  </div>
  <div class="abs view-note">Having Trouble Viewing it? <span>View Online</span></div>
</header>

<section class="offer">
  <div class="abs hero-photo" role="img" aria-label="Smiling agent in a dark suit standing before a suburban house under a blue sky"></div>
  <div class="abs offer-box"><em>Free</em> Property<br>Management<br>For 2 Months!</div>
</section>

<section class="benefits">
  <p class="abs intro">For over <b>10 years</b>, Daniel Marsh and his team have been looking after property<br>investors throughout Sydney. As a Quellbrook Property client your benefits will include:</p>

  <div class="abs benefit" style="left:7px">
    <svg width="196" height="196" viewBox="0 0 196 196" aria-hidden="true"><circle cx="98" cy="98" r="98" fill="#000"/><g fill="none" stroke="#fff" stroke-width="5" stroke-linejoin="round"><path d="M56 100l34-30 20 18M64 94v44h46v-30"/><rect x="80" y="112" width="14" height="14"/><circle cx="124" cy="78" r="20"/></g><text x="124" y="87" text-anchor="middle" font-family="Arimo,sans-serif" font-size="26" fill="#fff">$</text></svg>
    <p>OPTIMAL RENT</p>
  </div>
  <div class="abs benefit" style="left:300px">
    <svg width="196" height="196" viewBox="0 0 196 196" aria-hidden="true"><circle cx="98" cy="98" r="98" fill="#000"/><g fill="none" stroke="#fff" stroke-width="5" stroke-linejoin="round"><path d="M62 70l16-14 14 14-8 8 58 58-10 10-58-58-8 8z"/><path d="M134 60a16 16 0 0 0-20 20l-54 54 8 8 54-54a16 16 0 0 0 20-20l-10 10-8-8z"/></g></svg>
    <p>REDUCE REPAIRS &amp;<br>MAINTENANCE BILLS</p>
  </div>
  <div class="abs benefit" style="left:602px">
    <svg width="196" height="196" viewBox="0 0 196 196" aria-hidden="true"><circle cx="98" cy="98" r="98" fill="#000"/><g fill="none" stroke="#fff" stroke-width="5" stroke-linejoin="round"><path d="M70 90l30-26 30 26M78 84v24h44V84"/><path d="M50 126c14-6 28-8 42-2h22c6 0 6 8 0 8H94M114 128l24-10c6-2 10 4 4 8l-30 16H82l-20 6"/></g></svg>
    <p>REDUCED VACANCY</p>
  </div>
  <div class="abs benefit" style="left:888px">
    <svg width="196" height="196" viewBox="0 0 196 196" aria-hidden="true"><circle cx="98" cy="98" r="98" fill="#000"/><g fill="none" stroke="#fff" stroke-width="5" stroke-linejoin="round"><path d="M54 100l44-38 44 38M64 92v46h68V92"/><path d="M58 128l30-28 16 14 34-36M120 76h20v20"/></g></svg>
    <p>LEASE YOUR<br>PROPERTY FASTER</p>
  </div>
</section>

<section class="latest-articles">
  <div class="abs articles"></div>
  <h2 class="abs section-title articles-title">Latest Articles</h2>

  <div class="abs article-photo" style="left:60px;background:linear-gradient(135deg,#c9a05a 0%,#e7c48a 40%,#b9c7a2 60%,#efe9d8 100%)" role="img" aria-label="Model house on stacked banknotes beside a notepad and pen"></div>
  <h3 class="abs article-title" style="left:60px">Lorem ipsum dolor</h3>
  <p class="abs article-body" style="left:60px">Lorem ipsum dolor sit amet, consectetur adipiscing elit. Duis quis lectus at arcu egestas fringilla fermentum eget ipsum. Vestibulum hendrerit dignissim nunc vel volutpat. Nulla</p>
  <div class="abs read-more" style="left:62px">read more</div>

  <div class="abs article-photo" style="left:630px;background:linear-gradient(160deg,#6b4a3a 0%,#8b5e48 35%,#7fb7d9 60%,#5f8c4a 100%)" role="img" aria-label="Happy couple outside a brick home beside a sold sign"></div>
  <h3 class="abs article-title" style="left:630px">Lorem ipsum dolor</h3>
  <p class="abs article-body" style="left:630px">Lorem ipsum dolor sit amet, consectetur adipiscing elit. Duis quis lectus at arcu egestas fringilla fermentum eget ipsum. Vestibulum hendrerit dignissim nunc vel volutpat. Nulla</p>
  <div class="abs read-more" style="left:632px">read more</div>
</section>

<section class="director">
  <div class="abs director-photo" role="img" aria-label="Portrait of the company director"></div>
  <h2 class="abs section-title director-title">About the Director</h2>
  <p class="abs director-bio">Lorem ipsum dolor sit amet, consectetur adipiscing elit. Duis quis lectus at arcu egestas fringilla fermentum eget ipsum. Vestibulum hendrerit dignissim nunc vel volutpat. Nulla facilisi.</p>
  <div class="abs social-square" style="left:340px;background:#3b5a9a" aria-label="Social profile"></div>
  <div class="abs social-square" style="left:436px;background:#1d6fa5" aria-label="Professional profile"></div>
</section>

<footer>
  <div class="abs footer"></div>
  <div class="abs widget-photo" role="img" aria-label="Small director portrait"></div>
  <div class="abs widget-name">Quellbrook Property</div>
  <div class="abs like-btn"><i></i>Like</div>
  <div class="abs widget-rule"></div>
  <div class="abs widget-count">508 people like <span>Quellbrook Property</span>.</div>

  <div class="abs menu-head" style="left:408px">BUYERS AGENT</div>
  <ul class="abs menu-list" style="left:408px">
    <li>Need Help Buying Home?</li>
    <li>Buying an Investment Property?</li>
    <li>Buying a Commercial Property?</li>
  </ul>
  <div class="abs menu-head" style="left:854px">PROPERTY ADVICE</div>
  <ul class="abs menu-list" style="left:854px">
    <li>Need Property Advice?</li>
    <li>Need Property Appraisal?</li>
    <li>Need Help Negotiating?</li>
  </ul>

  <div class="abs bottom-bar">
    <span>Copyright 2014 QuellbrookProperty. All Rights Reserved.</span>
    <span>View Online &nbsp;|&nbsp; Unsubscribe</span>
  </div>
</footer>

</body>
</html>
```